EXPEDITE! Business Card For a Private Equity Firm
Fresh and Sleek
EXPEDITE!  Business Card For a Private Equity Firm - Financial Services
Creative Brief
Bright & Fun-filled
Ned Rusholt
Managing Partner
712 Larkmoor Street New York, NY 10032
ned@vorumbra-example.com
www.vorumbra-example.com
Looking for a fresh look on our new business cards. We have had previous designs on Plenavox for similar companies, but, now is time to refresh the look! Please submit as many design as possible. We will give you fast, efficient feedback!
Vorumbra Vorumbra
All. We also need email signatures and letterhead. Please provide.

```html
<!DOCTYPE html>
<html lang="en">
<head>
<meta charset="utf-8">
<title>Vorumbra Business Card</title>
<link href="https://fonts.googleapis.com/css2?family=Cinzel:wght@600&family=Open+Sans:wght@400;600&display=swap" rel="stylesheet">
<style>
  :root {
    --bg: #e4e4e2;
    --navy-deep: #0b2a6b;
    --navy: #1a4ea3;
    --blue-bright: #2f86cf;
    --sky: #3aa2dc;
    --card-white: #f7f8fa;
    --silver: #b9bec6;
    --silver-dark: #7c838d;
    --ink-blue: #1d5fa8;
    --ink-grey: #6a717b;
    --white: #ffffff;
  }
  * { margin: 0; padding: 0; box-sizing: border-box; }
  html, body { width: 1200px; height: 840px; overflow: hidden; background: var(--bg); }
  .sheet {
    width: 1200px; height: 840px; position: relative;
    font-family: "Open Sans", Arial, sans-serif;
  }
  .card {
    position: absolute; width: 640px; height: 366px; left: 280px;
    overflow: hidden; box-shadow: 0 6px 18px rgba(0,0,0,.18);
  }

  /* Front */
  .card-front {
    top: 30px;
    background: radial-gradient(ellipse at 30% 35%, var(--blue-bright) 0%, var(--navy) 45%, var(--navy-deep) 100%);
  }
  .front-brand {
    position: absolute; right: 48px; top: 150px; text-align: right; color: var(--white);
  }
  .front-name {
    font-family: "Cinzel", "Times New Roman", serif; font-weight: 600;
    font-size: 52px; letter-spacing: 2px; line-height: 1;
  }
  .front-web {
    margin-top: 8px; font-size: 14px; letter-spacing: 3px; opacity: .9;
  }

  /* Back */
  .card-back { top: 436px; background: var(--card-white); }
  .back-shapes { position: absolute; inset: 0; }
  .brand-mark {
    position: absolute; left: 190px; top: 44px; display: flex; align-items: center; gap: 10px;
  }
  .brand-dot { width: 26px; height: 26px; border-radius: 50%; background: var(--ink-blue); }
  .brand-name {
    font-family: "Cinzel", "Times New Roman", serif; font-weight: 600;
    font-size: 44px; letter-spacing: 1px; color: var(--ink-blue); line-height: 1;
  }
  .person { position: absolute; left: 34px; top: 52px; }
  .person-name { font-size: 17px; color: var(--ink-blue); }
  .person-title { font-size: 11px; color: var(--ink-grey); margin-top: 2px; }
  .back-web {
    position: absolute; right: 46px; top: 210px;
    font-size: 17px; letter-spacing: 3px; color: var(--ink-grey);
  }
  .contact {
    position: absolute; left: 30px; top: 262px; color: var(--white);
    font-size: 11px; line-height: 16px; display: flex; gap: 26px;
  }
  .contact-list li { list-style: none; display: flex; align-items: center; gap: 6px; }
  .contact-list svg { width: 10px; height: 10px; fill: var(--white); flex: none; }
</style>
</head>
<body>
<main class="sheet">

  <section class="card card-front" aria-label="Card front">
    <div class="front-brand">
      <div class="front-name">VORUMBRA</div>
      <div class="front-web">www.vorumbra-example.com</div>
    </div>
  </section>

  <section class="card card-back" aria-label="Card back">
    <svg class="back-shapes" viewBox="0 0 640 366" preserveAspectRatio="none">
      <defs>
        <linearGradient id="bandBlue" x1="0" y1="0" x2="1" y2="0">
          <stop offset="0" stop-color="var(--sky)"/>
          <stop offset="1" stop-color="var(--navy)"/>
        </linearGradient>
        <linearGradient id="silverLine" x1="0" y1="0" x2="1" y2="0">
          <stop offset="0" stop-color="var(--silver-dark)"/>
          <stop offset="1" stop-color="var(--silver)"/>
        </linearGradient>
      </defs>
      <polygon points="0,138 170,138 190,160 640,160 640,168 186,168 166,146 0,146" fill="url(#silverLine)"/>
      <polygon points="0,245 250,245 272,268 640,268 640,366 0,366" fill="url(#bandBlue)"/>
      <polygon points="250,238 640,238 640,244 276,244 254,264 250,264" fill="url(#silverLine)"/>
      <rect x="260" y="340" width="380" height="26" fill="var(--navy-deep)" opacity=".55"/>
    </svg>

    <div class="person">
      <div class="person-name">Ned Rusholt</div>
      <div class="person-title">Managing Partner</div>
    </div>
    <div class="brand-mark">
      <span class="brand-dot"></span>
      <span class="brand-name">VORUMBRA</span>
    </div>

    <div class="back-web">www.vorumbra-example.com</div>

    <div class="contact">
      <address style="font-style:normal">712 Larkmoor Street<br>New York, NY 10032</address>
      <ul class="contact-list">
        <li><svg viewBox="0 0 10 10"><path d="M2 0h2l1 3-1.5 1a6 6 0 0 0 2.5 2.5L7 5l3 1v2c0 1-1 2-2 2A8 8 0 0 1 0 2c0-1 1-2 2-2z"/></svg>(212) 555-0148</li>
        <li><svg viewBox="0 0 10 10"><rect x="1" y="3" width="8" height="6"/><rect x="3" y="0" width="4" height="3"/></svg>(212) 555-0193</li>
        <li><svg viewBox="0 0 10 10"><path d="M0 2h10v6H0zM0 2l5 3 5-3" /></svg>ned@vorumbra-example.com</li>
      </ul>
    </div>
  </section>

</main>
</body>
</html>
```